Quorra Desk Relay Chat Monitor Interface

We have a live help chat software that we need a new chat monitor interface designed for. Something that will be easy to make responsive. I will provide screen shots of the current interface and a picture of the new admin back-end that we want it to look similar too. This project should be fairly straight forward and easy. See below.

Important Notes:

1. You DO NOT need to worry about the actual list of visitors on the site in the middle as that will be handled by the grid system we use.

2. We have decided to eliminate the logo from the monitor all together to make it more compact. Just the words "Quorra Desk Relay" and a copyright notice will be enough.

3. We want the chat monitor interface to utilize the same colors and look as the new admin interface if possible. See attached "new_admin_interface.png" image.

4. Although I want to utilize the same colors as the admin area, it should NOT utilize the same header and footer as the admin area. I only referenced the admin area so that you can get color ideas from it. Consider it a popup window and assume the same amount of space will be used. Although it will have the ability to be resized we must not waste space.

Target Market(s)

N/A

Industry/Entity Type

Software

Number of Pages Required

1 page

Requirements
Must have
• See Description.
Nice to have
• See Description.
Should not have
• See Description.

```html
<!DOCTYPE html>
<html lang="en">
<head>
<meta charset="utf-8">
<title>Quorra Desk Relay – Chat Monitor</title>
<link rel="stylesheet" href="https://fonts.googleapis.com/css2?family=Open+Sans:wght@400;600;700&display=swap">
<style>
:root{
  --bar:#2c3b4b;
  --bar-text:#ffffff;
  --page:#e8e8e8;
  --panel:#eef1f5;
  --panel-white:#ffffff;
  --line:#d4d7db;
  --head-top:#fbfbfb;
  --head-bottom:#e6e6e6;
  --text:#333a42;
  --icon:#3a4450;
  --label:#8a8a8a;
  --value-bg:#efedec;
  --green:#7cb518;
  --green-dark:#3b8a2a;
  --online:#4a9e3c;
}
*{box-sizing:border-box;margin:0;padding:0}
html,body{width:1200px;height:960px;overflow:hidden}
body{background:var(--page);font-family:"Open Sans",Arial,sans-serif;color:var(--text);font-size:16px;position:relative}
svg{display:block}

.topbar{position:absolute;left:0;top:0;width:1200px;height:52px;background:var(--bar);color:var(--bar-text);display:flex;align-items:center;padding-left:22px;font-size:17px}
.topbar .item{display:flex;align-items:center;gap:9px;margin-right:22px}
.status-select{width:145px;height:29px;background:#fff;border-radius:3px;color:var(--text);display:flex;align-items:center;padding:0 10px;gap:9px;font-size:16px;margin-left:-10px;margin-right:30px;position:relative}
.status-select .dot{width:10px;height:10px;border-radius:50%;background:var(--online)}
.status-select .caret{position:absolute;right:9px;top:6px}
.brand{position:absolute;right:22px;top:12px;font-weight:700;font-size:22px;letter-spacing:.3px;color:#fff}

.panel{position:absolute;background:var(--panel);border:1px solid var(--line);border-radius:3px;overflow:hidden}
.visitors{left:12px;top:64px;width:1176px;height:421px}
table.grid{border-collapse:collapse;width:100%}
.grid th{height:53px;font-weight:400;font-size:16px;text-align:left;padding-left:20px;background:linear-gradient(var(--head-top),var(--head-bottom));border-right:1px solid var(--line);border-bottom:1px solid var(--line)}
.grid th.c,.grid td.c{text-align:center;padding-left:0}
.grid td{height:49px;font-size:15.5px;background:#fff;border-right:1px solid var(--line);border-bottom:1px solid var(--line);padding-left:20px;white-space:nowrap}
.grid td.loc{padding-left:20px;max-width:466px;overflow:hidden;text-overflow:ellipsis;font-size:15px}
.grid tr td:last-child,.grid tr th:last-child{border-right:none}
.ipcell{display:flex;align-items:center;gap:12px;padding-left:2px}
.op{color:var(--green-dark)}
.badge{width:22px;height:22px;margin:0 auto;background:var(--icon)}
.badge.round{border-radius:50%}
.badge.sq{border-radius:3px;width:20px;height:20px}

.details{left:12px;top:497px;width:912px;height:436px;background:var(--panel-white)}
.tabs{height:60px;background:linear-gradient(var(--head-top),var(--head-bottom));border-bottom:1px solid var(--line);display:flex;align-items:flex-end;padding-left:12px}
.tab{height:44px;display:flex;align-items:center;gap:9px;padding:0 22px;font-size:17px}
.tab.active{background:#fff;border:1px solid var(--line);border-bottom:none;border-radius:4px 4px 0 0;height:45px;margin-bottom:-1px}
table.info{position:absolute;left:31px;top:76px;width:854px;border-collapse:separate;border-spacing:0 2px}
.info th{width:161px;background:var(--label);color:#fff;font-weight:400;font-size:16px;text-align:right;padding-right:13px;height:37px}
.info td{background:var(--value-bg);padding-left:14px;font-size:16px;border-left:2px solid #fff}
.info td .flagbox{display:inline-flex;vertical-align:middle;margin-right:10px}
.link{color:var(--green);font-weight:700}

.operators{left:936px;top:497px;width:252px;height:436px;background:var(--panel-white)}
.operators .head{height:60px;background:linear-gradient(var(--head-top),var(--head-bottom));border-bottom:1px solid var(--line);display:flex;align-items:center;gap:10px;padding-left:19px;font-size:17px}
.operator{display:flex;align-items:center;gap:12px;padding:22px 0 0 20px;font-size:16px}
</style>
</head>
<body>

<header class="topbar">
  <div class="item">
    <svg width="20" height="12" viewBox="0 0 20 12"><rect x="0" y="0" width="20" height="12" rx="6" fill="#fff"/><circle cx="6" cy="6" r="3.6" fill="var(--bar)"/></svg>
    Status
  </div>
  <div class="status-select"><span class="dot"></span>Online
    <svg class="caret" width="8" height="16" viewBox="0 0 8 16"><path d="M1 6 4 2 7 6Z M1 10 4 14 7 10Z" fill="#555"/></svg>
  </div>
  <div class="item">
    <svg width="19" height="15" viewBox="0 0 19 15"><path d="M0 2h6l2 2h8v2H4L1 14H0Z M4 7h15l-3 8H1Z" fill="#fff"/></svg>
    File
  </div>
  <div class="item">
    <svg width="15" height="15" viewBox="0 0 15 15"><path d="M15 0 0 6.5 7 8 8.5 15Z" fill="#fff"/></svg>
    Actions
  </div>
  <div class="brand">Quorra Desk Relay</div>
</header>

<section class="panel visitors">
  <table class="grid">
    <colgroup><col style="width:188px"><col style="width:163px"><col style="width:109px"><col style="width:87px"><col style="width:466px"><col style="width:95px"><col></colgroup>
    <thead><tr><th>IP Address</th><th>Status</th><th class="c">Duration</th><th class="c">Pages</th><th>Location</th><th class="c">Browser</th><th class="c">OS</th></tr></thead>
    <tbody>
      <tr>
        <td><div class="ipcell"><svg width="22" height="19" viewBox="0 0 22 19"><ellipse cx="11" cy="8" rx="11" ry="8" fill="var(--icon)"/><path d="M3 13 1 19 8 15Z" fill="var(--icon)"/></svg>71.104.58.59</div></td>
        <td>Chatting <span class="op">“mbrenner”</span></td>
        <td class="c">0:40:01</td><td class="c">17</td>
        <td class="loc">https://www.lanternhostgrid.com/billing/admin/supporttickets...</td>
        <td class="c"><div class="badge round"></div></td><td class="c"><div class="badge sq"></div></td>
      </tr>
      <tr>
        <td><div class="ipcell"><svg width="22" height="20" viewBox="0 0 22 20"><circle cx="11" cy="5.5" r="5" fill="var(--icon)"/><path d="M3 20v-4a6 6 0 0 1 6-5h4a6 6 0 0 1 6 5v4Z" fill="var(--icon)"/></svg>71.104.58.59</div></td>
        <td>In Site</td><td class="c">0:40:01</td><td class="c">1</td>
        <td class="loc">https://www.lanternhostgrid.com/billing/admin/supporttickets...</td>
        <td class="c"><div class="badge round"></div></td><td class="c"><div class="badge sq"></div></td>
      </tr>
      <tr>
        <td><div class="ipcell"><svg width="22" height="20" viewBox="0 0 22 20"><circle cx="11" cy="5.5" r="5" fill="var(--icon)"/><path d="M3 20v-4a6 6 0 0 1 6-5h4a6 6 0 0 1 6 5v4Z" fill="var(--icon)"/></svg>71.104.58.59</div></td>
        <td>In Site</td><td class="c">0:40:01</td><td class="c">1</td>
        <td class="loc">https://www.lanternhostgrid.com/billing/admin/supporttickets...</td>
        <td class="c"><div class="badge round"></div></td><td class="c"><div class="badge sq"></div></td>
      </tr>
    </tbody>
  </table>
</section>

<section class="panel details">
  <nav class="tabs">
    <div class="tab active"><svg width="17" height="17" viewBox="0 0 17 17"><circle cx="8.5" cy="8.5" r="8.5" fill="var(--icon)"/><rect x="7.3" y="7" width="2.4" height="6" fill="#fff"/><circle cx="8.5" cy="4.6" r="1.4" fill="#fff"/></svg>Visitors Info</div>
    <div class="tab"><svg width="18" height="14" viewBox="0 0 18 14"><rect x="0.8" y="0.8" width="16.4" height="12.4" fill="none" stroke="var(--icon)" stroke-width="1.6"/><path d="M3 4h2M7 4h8M3 7h2M7 7h8M3 10h2M7 10h8" stroke="var(--icon)" stroke-width="1.5"/></svg>Footprints</div>
    <div class="tab"><svg width="19" height="15" viewBox="0 0 19 15"><ellipse cx="7" cy="6" rx="7" ry="5" fill="var(--icon)"/><ellipse cx="13" cy="9" rx="6" ry="4.3" fill="var(--icon)"/><path d="M2 9 1 14 6 11Z M16 12l2 3-5-2Z" fill="var(--icon)"/></svg>Chat</div>
  </nav>
  <table class="info">
    <tr><th>IP Address</th><td><span class="flagbox"><svg width="40" height="21" viewBox="0 0 40 21"><rect width="40" height="21" fill="#fff"/><g fill="#c0282d"><rect y="0" width="40" height="1.6"/><rect y="3.2" width="40" height="1.6"/><rect y="6.4" width="40" height="1.6"/><rect y="9.6" width="40" height="1.6"/><rect y="12.8" width="40" height="1.6"/><rect y="16" width="40" height="1.6"/><rect y="19.2" width="40" height="1.8"/></g><rect width="17" height="11.2" fill="#2b3f86"/></svg></span>199.201.102.196</td></tr>
    <tr><th>Hostname</th><td>199-201-102-196.ut.corvalnet.net</td></tr>
    <tr><th>Referer</th><td class="link">https://searchpoint.com</td></tr>
    <tr><th>User Agent</th><td>199-201-102-196.ut.corvalnet.net</td></tr>
    <tr><th>Browser &amp; OS</th><td>Brisa 52.0.2743.116 - Fenestra 7</td></tr>
    <tr><th>Resolution</th><td>1920 x 1080</td></tr>
    <tr><th>Local Time</th><td>4:30:30 PM</td></tr>
    <tr><th>Time Online</th><td>0:24:09</td></tr>
    <tr><th>Transcripts</th><td class="link">0</td></tr>
  </table>
</section>

<aside class="panel operators">
  <div class="head"><svg width="18" height="18" viewBox="0 0 18 18"><circle cx="9" cy="9" r="7.5" fill="none" stroke="var(--icon)" stroke-width="3"/><circle cx="9" cy="9" r="3" fill="#fff" stroke="var(--icon)" stroke-width="1.4"/><path d="M4 4l3 3M14 4l-3 3M4 14l3-3M14 14l-3-3" stroke="#fff" stroke-width="1.6"/></svg>Operators</div>
  <div class="operator"><svg width="16" height="17" viewBox="0 0 22 20"><circle cx="11" cy="5.5" r="5" fill="var(--icon)"/><path d="M3 20v-4a6 6 0 0 1 6-5h4a6 6 0 0 1 6 5v4Z" fill="var(--icon)"/></svg>Dalen R</div>
</aside>

</body>
</html>
```